Lantern Journeys - Luxury, Theme, Guided Tours

Lan-journeys.com Lantern Journeys is being formed to create, sell and deliver to affluent baby boomers and mature adults, outstanding, memorable, boutique, luxury, guided theme tours to iconic North American destinations. These themes will revolve around activities and interests common to our target market, i.e. Culture, Culinary, Historic, Golf, Shopping etc. Our tours will include unique and enjoyable “wow” opportunities unavailable to guests were they to travel “on their own,” i.e. exclusive access, experiences and events, we arrange. Another critical component of our value proposition will be the camaraderie established among guests by marketing (and packaging) tours to specific markets. This will allow guests to tour, in small group sizes, with peers from their local community, with the opportunity to build new friendships that may flourish into the future.

Target Market(s)

Target Audience: Affluent, well-traveled, educated, sophisticated, fun, curious, brand-conscious, social senior/boomer ladies traveling with husband/partner or girlfriend(s)Brand Cohorts: Hallowell, Vescia, Ospren, Marlowe

Industry/Entity Type

Tourism

Font styles to use
Serif

Colors
3176b5
ffffff
fbf289

Requirements
Must have
• "Open" area at top to add specific Tour Names and destinations - using design as template. Colors complementary to those used in logo.
• On Back:
• Luxury Guided Theme Adventures and Tours
• Designed Especially For Mature Adults - "Boomers"
• Small Group of Local Peers Traveling Together
• Executive Mini Coach Transportation
• Finest Boutique Hotels
• Award - Winning Restaurants and Chefs
• Exclusive and Unique Experiences, Events, Personalities and Tours
• Adventure and Tour Themes:
• Culinary & Cultural Trail
• Top Golf Resorts
• Historic Times, Sights and Cities
• Shopping!
• High Culture
• Nature
• Photography
• Music
• Wineries, Breweries and Distilleries
• Contact us today for all upcoming adventures and tours:
• Address: 3127 Brookmere Ln. Suite410 Raleigh, NC 27318 Phone: 919.555.0142 Email: info@lan-journeys.com www.lan-journeys.com 8am - 8pm EST
• Referrer name space
Nice to have
• antique compass, map

```html
<!DOCTYPE html>
<html lang="en">
<head>
<meta charset="utf-8">
<title>Lantern Journeys – Luxury Guided Theme Adventures and Tours</title>
<link rel="stylesheet" href="https://fonts.googleapis.com/css2?family=PT+Sans:ital,wght@0,400;0,700;1,700&family=PT+Sans+Narrow:wght@400;700&display=swap">
<style>
  :root {
    --brand-blue: #3176b5;
    --light-blue: #6fa6d6;
    --icon-ring: #9cc3e6;
    --ink: #232a33;
    --white: #ffffff;
    --soft-yellow: #fbf289;
    --map-gold: #c9a467;
    --map-cream: #efe2c3;
    --map-brown: #8a6a3e;
  }
  * { box-sizing: border-box; margin: 0; padding: 0; }
  html, body { width: 1200px; height: 2612px; overflow: hidden; background: var(--white); }
  .flyer {
    position: relative;
    width: 1200px;
    height: 2612px;
    overflow: hidden;
    background: var(--white);
    font-family: "PT Sans", sans-serif;
    color: var(--ink);
  }
  .top-wash {
    position: absolute;
    left: 0; top: 0;
    width: 1200px; height: 700px;
    background: linear-gradient(180deg, #e9f1f9 0%, var(--white) 100%);
  }
  .map-art {
    position: absolute;
    left: 0; top: 640px;
    width: 1200px; height: 1340px;
    background:
      radial-gradient(ellipse 420px 420px at 300px 1000px, rgba(138,106,62,0.5), rgba(138,106,62,0) 70%),
      radial-gradient(ellipse 650px 420px at 950px 1000px, rgba(201,164,103,0.6), rgba(201,164,103,0) 75%),
      linear-gradient(180deg, rgba(255,255,255,1) 0%, rgba(239,226,195,0.6) 25%, var(--map-cream) 48%, var(--map-gold) 80%, #b48b52 100%);
  }

  .headline {
    position: absolute;
    left: 70px; top: 60px;
    font-family: "PT Sans Narrow", sans-serif;
    font-weight: 400;
    font-size: 100px;
    line-height: 122px;
    color: var(--brand-blue);
  }
  .tagline {
    position: absolute;
    left: 70px; top: 344px;
    font-weight: 700;
    font-style: italic;
    font-size: 43px;
    line-height: 56px;
    color: var(--ink);
  }
  .tagline .accent { color: var(--brand-blue); }
  .tagline-rule {
    position: absolute;
    left: 70px; top: 408px;
    width: 1060px; height: 3px;
    background: var(--brand-blue);
  }

  .features {
    position: absolute;
    left: 70px; top: 435px;
    width: 1080px;
    list-style: none;
  }
  .feature {
    position: relative;
    padding-left: 95px;
    font-size: 44px;
    line-height: 56px;
    margin-bottom: 15px;
  }
  .feature > svg {
    position: absolute;
    left: 0; top: 6px;
    width: 44px; height: 44px;
  }
  .themes { list-style: none; }
  .theme {
    position: relative;
    padding-left: 34px;
    font-size: 37px;
    line-height: 62px;
  }
  .theme::before {
    content: "";
    position: absolute;
    left: 6px; top: 27px;
    width: 11px; height: 11px;
    border-radius: 50%;
    background: var(--ink);
  }

  .client-name {
    position: absolute;
    left: 860px; top: 1245px;
    display: flex;
    align-items: center;
    gap: 12px;
    font-weight: 700;
    font-size: 30px;
    color: var(--brand-blue);
  }
  .client-name .mark { width: 24px; height: 24px; background: var(--brand-blue); }

  .referrer-label {
    position: absolute;
    left: 70px; top: 2002px;
    font-size: 44px;
    line-height: 56px;
    color: var(--ink);
  }

  .contact-shape { position: absolute; left: 0; top: 1980px; }

  .contact-title {
    position: absolute;
    left: 80px; top: 2180px;
    font-weight: 700;
    font-size: 35px;
    line-height: 50px;
    color: var(--white);
  }
  .contact-row {
    position: absolute;
    left: 80px;
    display: flex;
    align-items: center;
    gap: 20px;
    font-weight: 700;
    color: var(--white);
  }
  .contact-row svg { width: 40px; height: 40px; flex: none; }
  .row-address { top: 2316px; font-size: 30px; }
  .row-phone { top: 2380px; font-size: 48px; }
  .row-email { top: 2458px; font-size: 32px; }
  .contact-aside {
    position: absolute;
    left: 765px;
    font-weight: 700;
    color: var(--white);
  }
  .hours { top: 2380px; font-size: 46px; }
  .website { top: 2458px; font-size: 32px; }
</style>
</head>
<body>
<main class="flyer">
  <div class="top-wash"></div>
  <div class="map-art" role="img" aria-label="Antique brass compass resting on an old sepia world map"></div>

  <h1 class="headline">Luxury Guided Theme<br>Adventures and Tours</h1>
  <p class="tagline">Designed Especially For Mature Adults - <span class="accent">"Boomers"</span></p>
  <div class="tagline-rule"></div>

  <ul class="features">
    <li class="feature"><svg viewBox="0 0 50 50"><circle cx="25" cy="25" r="22" fill="var(--white)" stroke="var(--icon-ring)" stroke-width="4"/><path d="M21 15 L31 25 L21 35" fill="none" stroke="var(--brand-blue)" stroke-width="5" stroke-linecap="round" stroke-linejoin="round"/></svg>Small Group of Local Peers Traveling Together</li>
    <li class="feature"><svg viewBox="0 0 50 50"><circle cx="25" cy="25" r="22" fill="var(--white)" stroke="var(--icon-ring)" stroke-width="4"/><path d="M21 15 L31 25 L21 35" fill="none" stroke="var(--brand-blue)" stroke-width="5" stroke-linecap="round" stroke-linejoin="round"/></svg>Executive Mini Coach Transportation</li>
    <li class="feature"><svg viewBox="0 0 50 50"><circle cx="25" cy="25" r="22" fill="var(--white)" stroke="var(--icon-ring)" stroke-width="4"/><path d="M21 15 L31 25 L21 35" fill="none" stroke="var(--brand-blue)" stroke-width="5" stroke-linecap="round" stroke-linejoin="round"/></svg>Finest Boutique Hotels</li>
    <li class="feature"><svg viewBox="0 0 50 50"><circle cx="25" cy="25" r="22" fill="var(--white)" stroke="var(--icon-ring)" stroke-width="4"/><path d="M21 15 L31 25 L21 35" fill="none" stroke="var(--brand-blue)" stroke-width="5" stroke-linecap="round" stroke-linejoin="round"/></svg>Award - Winning Restaurants and Chefs</li>
    <li class="feature"><svg viewBox="0 0 50 50"><circle cx="25" cy="25" r="22" fill="var(--white)" stroke="var(--icon-ring)" stroke-width="4"/><path d="M21 15 L31 25 L21 35" fill="none" stroke="var(--brand-blue)" stroke-width="5" stroke-linecap="round" stroke-linejoin="round"/></svg>Exclusive and Unique Experiences, Events,<br>Personalities and Tours</li>
    <li class="feature"><svg viewBox="0 0 50 50"><circle cx="25" cy="25" r="22" fill="var(--white)" stroke="var(--icon-ring)" stroke-width="4"/><path d="M21 15 L31 25 L21 35" fill="none" stroke="var(--brand-blue)" stroke-width="5" stroke-linecap="round" stroke-linejoin="round"/></svg>Adventure and Tour Themes:
      <ul class="themes">
        <li class="theme">Culinary &amp; Cultural Trail</li>
        <li class="theme">Top Golf Resorts</li>
        <li class="theme">Historic Times, Sights and Cities</li>
        <li class="theme">Shopping</li>
        <li class="theme">High Culture</li>
        <li class="theme">Nature</li>
        <li class="theme">Photography</li>
        <li class="theme">Music</li>
        <li class="theme">Wineries, Breweries and Distilleries</li>
      </ul>
    </li>
  </ul>

  <div class="client-name"><span class="mark"></span>Lantern Journeys</div>

  <p class="referrer-label">Referrer Name:</p>

  <svg class="contact-shape" width="1200" height="632" viewBox="0 0 1200 632" aria-hidden="true">
    <path d="M0 140 C 420 132 860 100 1200 0 L1200 632 L0 632 Z" fill="var(--light-blue)"/>
    <path d="M0 160 C 430 152 870 125 1200 36 L1200 632 L0 632 Z" fill="var(--brand-blue)"/>
    <line x1="80" y1="322" x2="680" y2="322" stroke="var(--white)" stroke-width="2"/>
  </svg>

  <p class="contact-title">Contact us today for all<br>upcoming adventures and tours:</p>

  <p class="contact-row row-address">
    <svg viewBox="0 0 40 40"><circle cx="20" cy="20" r="19" fill="var(--white)"/><text x="20" y="28" text-anchor="middle" font-family="PT Sans, sans-serif" font-weight="700" font-size="22" fill="var(--brand-blue)">A</text></svg>
    3127 Brookmere Ln. Suite410 Raleigh, NC 27318
  </p>
  <p class="contact-row row-phone">
    <svg viewBox="0 0 40 40"><circle cx="20" cy="20" r="19" fill="var(--white)"/><text x="20" y="28" text-anchor="middle" font-family="PT Sans, sans-serif" font-weight="700" font-size="22" fill="var(--brand-blue)">P</text></svg>
    919.555.0142
  </p>
  <p class="contact-row row-email">
    <svg viewBox="0 0 40 40"><circle cx="20" cy="20" r="19" fill="var(--white)"/><text x="20" y="28" text-anchor="middle" font-family="PT Sans, sans-serif" font-weight="700" font-size="22" fill="var(--brand-blue)">E</text></svg>
    info@lan-journeys.com
  </p>
  <p class="contact-aside hours">8am - 8pm EST</p>
  <p class="contact-aside website">www.lan-journeys.com</p>
</main>
</body>
</html>
```